Flooring & Interior Design showroom

Just bought this business- Kestrel Lane Flooring & Interiors. Love our logo (we are on Kestrel Lane )and colors
Forest green, gold and black
Love that the back lists everything we do. We no longer have plenotilex but need to add in LVP/ SPC and need to take out vantor shadehub logo at the bottom and use the quib logo instead (maybe? open to suggestions)

Not in love with our cards- I want a higher end look
I hate the gradient poop color we have now.
Would love if they were all black - maybe or ??
or had a foil or embossing?

```html
<!DOCTYPE html>
<html lang="en">
<head>
<meta charset="utf-8">
<title>Kestrel Lane Flooring &amp; Interiors — Business Card</title>
<link rel="stylesheet" href="https://fonts.googleapis.com/css2?family=Cinzel:wght@600&family=Karla:wght@400;500;600&display=swap">
<style>
  :root {
    --forest: #1f5a36;
    --forest-light: #2f7a4b;
    --copper: #c58a62;
    --ink: #0d0d0d;
    --paper: #f3f2ef;
    --grey-text: #3a3a3a;
    --partner-grey: #8a9099;
    --stage: #2a2a2a;
  }
  * { margin: 0; padding: 0; box-sizing: border-box; }
  html, body { width: 1200px; height: 874px; overflow: hidden; }
  body {
    background: var(--stage);
    display: flex; flex-direction: column; align-items: center; justify-content: center;
    gap: 36px;
    font-family: "Karla", sans-serif;
  }
  .card { width: 640px; height: 366px; border-radius: 22px; overflow: hidden; position: relative; }

  /* Brand name set as plain text */
  .brand { display: flex; align-items: center; gap: 12px; }
  .brand-square { width: 16px; height: 16px; background: var(--forest-light); flex: none; }
  .brand-name {
    font-family: "Karla", sans-serif; font-weight: 600; color: var(--forest-light);
    line-height: 1.15;
  }

  /* Back of card */
  .card--back { background: var(--ink); color: #fff; text-align: center; }
  .card--back .brand { justify-content: center; padding-top: 48px; }
  .card--back .brand-name { font-size: 30px; }
  .tagline { font-size: 14px; color: var(--forest-light); margin-top: 8px; }
  .services { margin-top: 22px; font-size: 15px; line-height: 1.55; }
  .services .dot { color: var(--forest-light); margin: 0 5px; font-size: 11px; }
  .partners { display: flex; justify-content: center; align-items: center; gap: 30px; margin-top: 22px; }
  .partner { font-weight: 500; font-size: 19px; color: var(--partner-grey); }

  /* Front of card */
  .card--front { background: var(--paper); }
  .front-body { display: flex; height: 276px; }
  .front-brand { width: 300px; display: flex; align-items: center; padding-left: 36px; }
  .front-brand .brand-name { font-size: 24px; color: var(--forest); }
  .front-brand .brand-square { background: var(--forest); }
  .divider { width: 1px; background: #bdbdbd; margin: 46px 0 36px; }
  .contact { padding: 40px 0 0 30px; color: var(--grey-text); font-size: 15px; line-height: 1.42; }
  .person-name { font-family: "Cinzel", serif; font-weight: 600; font-size: 26px; color: var(--forest); letter-spacing: 1px; line-height: 1.1; }
  .person-role { color: var(--copper); font-size: 14px; margin-bottom: 8px; }
  .contact-line { display: flex; align-items: center; gap: 8px; }
  .contact-line svg { width: 13px; height: 13px; fill: var(--copper); flex: none; }
  .band-rule { height: 3px; background: var(--copper); margin-top: 4px; }
  .web-band {
    background: var(--forest); height: 83px; display: flex; align-items: center; justify-content: center;
    color: #e9ece8; font-size: 17px; letter-spacing: 6px; font-weight: 500;
  }
</style>
</head>
<body>

<section class="card card--back" aria-label="Card back">
  <div class="brand">
    <span class="brand-square"></span>
    <span class="brand-name">Kestrel Lane Flooring &amp; Interiors</span>
  </div>
  <div class="tagline">Home Town Service Since 1979</div>
  <p class="services">
    Area Rugs<span class="dot">●</span>Blinds<span class="dot">●</span>Carpet<span class="dot">●</span>Cork<span class="dot">●</span>Hardwood<span class="dot">●</span>Laminate<br>
    Sheers<span class="dot">●</span>Valances<span class="dot">●</span>Vinyl<span class="dot">●</span>Bed Spreads<span class="dot">●</span>Draperies<span class="dot">●</span>LVP/SPC<span class="dot">●</span>Fabric<br>
    Motorized Shades<span class="dot">●</span>Pillows<span class="dot">●</span>Shutters<span class="dot">●</span>Upholstery<span class="dot">●</span>Verticals
  </p>
  <div class="partners">
    <span class="partner">Larkmont Shades</span>
    <span class="partner">Quib</span>
  </div>
</section>

<section class="card card--front" aria-label="Card front">
  <div class="front-body">
    <div class="front-brand">
      <div class="brand">
        <span class="brand-square"></span>
        <span class="brand-name">Kestrel Lane<br>Flooring &amp; Interiors</span>
      </div>
    </div>
    <div class="divider"></div>
    <div class="contact">
      <div class="person-name">Eli Marston</div>
      <div class="person-role">Salesperson</div>
      <div>314 Kestrel Lane</div>
      <div>Seabrook CA 95010</div>
      <div class="contact-line">
        <svg viewBox="0 0 16 16"><path d="M3 1l3 3-2 2c1 2 3 4 5 5l2-2 3 3-2 3C6 15 1 10 1 3z"/></svg>555.201.0147
      </div>
      <div class="contact-line">
        <svg viewBox="0 0 16 16"><path d="M4 0h8v16H4zM5.5 2v10h5V2z"/></svg>555-318-2290
      </div>
      <div class="contact-line">
        <svg viewBox="0 0 16 16"><path d="M4 1h7v4H4zM1 6h14v7h-3v2H4v-2H1zM5 11v3h6v-3z"/></svg>555.406.7731
      </div>
      <div class="contact-line">
        <svg viewBox="0 0 16 16"><path d="M0 3h16v10H0zM1.5 4.5L8 9l6.5-4.5z"/></svg>eli@kestrellaneflooring.com
      </div>
      <div>CA Lic: 418072</div>
    </div>
  </div>
  <div class="band-rule"></div>
  <div class="web-band">WWW.KESTRELLANEFLOORING.COM</div>
</section>

</body>
</html>
```